Recruitment Package Design for Healthcare Organization

We need a brochure designed that matches the design of our website and logo. The focus of the brochure is to provide information about our organization and region to prospective physicians looking to join our team. I have the content already put together, but would like some imagery of local geography/activities to be incorporated into the design. I have attached the content document as well as an example we are wanting to model ours after.

Our website is: https://brightmarrowcare.ca/

Target Market(s)

Prospective physicians

Industry/Entity Type

Healthcare

Requirements
Must have
• Local imagery which I have attached.

```html
<!DOCTYPE html>
<html lang="en">
<head>
<meta charset="utf-8">
<title>Bright Marrow Care — Physician Recruitment Package</title>
<link href="https://fonts.googleapis.com/css2?family=Montserrat:ital,wght@0,400;0,500;0,600;0,700;1,400&display=swap" rel="stylesheet">
<style>
:root{
  --teal:#35d0dc;
  --teal-soft:#dcf5f8;
  --teal-faint:#eefafb;
  --teal-plus:#7fe2ea;
  --ink:#3b3b3b;
  --muted:#8a8a8a;
  --grey-band:#e6e6e6;
  --photo:#6b6b6b;
  --stage:#7d7d7d;
  --paper:#ffffff;
}
*{margin:0;padding:0;box-sizing:border-box}
html,body{width:1200px;height:4987px;overflow:hidden}
body{background:var(--stage);font-family:"Montserrat",sans-serif;color:var(--ink);position:relative}
.page{position:absolute;left:397px;width:406px;height:578px;background:var(--paper);overflow:hidden}
.sidebar{position:absolute;left:0;top:0;bottom:0;width:44px;background:var(--teal)}
.page-no{position:absolute;left:0;width:44px;top:22px;text-align:center;color:#fff;font-weight:700;font-size:20px}
.side-plus{position:absolute;left:2px;top:270px;width:30px;height:30px}
.content{position:absolute;left:52px;right:14px;top:22px;font-size:6.3px;line-height:1.38}
.content p{margin-bottom:6px}
h2{color:var(--teal);font-weight:600;font-size:14.5px;line-height:1.1;margin-bottom:7px;position:relative}
h2 .ghost{position:absolute;left:130px;top:-8px;font-size:38px;color:#f1f1f1;font-weight:500;z-index:-1;white-space:nowrap}
h3{color:var(--teal);font-weight:600;font-size:13px;margin:8px 0 5px}
.lead{color:var(--teal);font-weight:600}
.quote{font-style:italic;color:var(--muted)}
ul.bullets{list-style:none;margin:0 0 6px 12px}
ul.bullets li{margin-bottom:5px}
ul.bullets li::before{content:"• ";color:var(--teal)}
.sub{color:var(--muted);font-size:7px;margin:-4px 0 8px}
.decor{position:absolute}
.cols{display:flex;gap:30px}
.cols>div{flex:1}
.list-title{color:var(--teal);font-weight:600;font-size:7.5px;margin-bottom:3px}
.mini{list-style:none;font-size:5px;line-height:1.5;color:var(--muted);margin-left:10px}
.mini li::before{content:"• "}
.links{font-size:6.5px;font-weight:600;margin-left:12px;line-height:2}
.brand{position:absolute;right:30px;top:60px;display:flex;align-items:center;gap:8px}
.brand-mark{width:22px;height:22px;border:2px solid var(--teal)}
.brand-name{color:var(--teal);font-weight:500;font-size:15px}
.intro-text{width:200px;min-height:160px}
</style>
</head>
<body>

<section class="page" style="top:226px">
  <svg class="decor" width="406" height="578" viewBox="0 0 406 578" aria-hidden="true">
    <polygon points="0,0 270,0 0,270" fill="var(--grey-band)"/>
    <polygon points="406,260 406,578 90,578" fill="var(--teal-soft)"/>
    <g transform="rotate(45 195 290)">
      <rect x="102" y="197" width="186" height="186" rx="36" fill="none" stroke="var(--photo)" stroke-width="3"/>
      <rect x="112" y="207" width="186" height="186" rx="36" fill="none" stroke="var(--photo)" stroke-width="3"/>
    </g>
    <g fill="var(--teal-soft)"><rect x="40" y="440" width="20" height="70"/><rect x="15" y="465" width="70" height="20"/></g>
    <g fill="var(--grey-band)"><rect x="340" y="130" width="8" height="30"/><rect x="329" y="141" width="30" height="8"/></g>
  </svg>
  <svg class="decor" style="left:0;top:0" width="406" height="578" role="img" aria-label="Okanagan lakeside landscape photograph">
    <g transform="rotate(45 210 305)"><rect x="122" y="217" width="176" height="176" rx="32" fill="var(--photo)"/></g>
  </svg>
  <div class="brand"><span class="brand-mark"></span><span class="brand-name">Bright Marrow Care</span></div>
</section>

<section class="page" style="top:884px">
  <div class="sidebar"><div class="page-no">1</div>
    <svg class="side-plus" viewBox="0 0 30 30" aria-hidden="true"><rect x="11" y="0" width="8" height="30" fill="var(--teal-plus)"/><rect x="0" y="11" width="30" height="8" fill="var(--teal-plus)"/></svg></div>
  <svg class="decor" style="left:270px;top:450px" width="110" height="110" aria-hidden="true"><rect x="38" y="0" width="34" height="110" fill="var(--teal-faint)"/><rect x="0" y="38" width="110" height="34" fill="var(--teal-faint)"/></svg>
  <div class="content">
    <h2>CEO Message<span class="ghost">Message</span></h2>
    <p><span class="lead">Thank you for your interest in Bright Marrow Care</span> – whether you are a recent graduate looking to establish your practice or a veteran physician looking for a change. I am confident you can find your healthcare home here. It is my privilege to help lead an organisation that is truly committed to creating the best possible experiences and outcomes for our patients and the communities we serve. As the Okanagan's population has boomed over the last decade, there is ever greater need to provide residents with access to essential healthcare services. Our time-tested and sustainable operating model has enabled us to not only survive, but thrive through the many challenges that the past 5 years have presented the healthcare industry.</p>
    <p>Founded in 2016, Bright Marrow Care is an established organisation with a strong reputation in the communities we serve. From a business perspective, our revenue is healthy and our trajectory is positive. The numbers back this up:</p>
    <ul class="bullets">
      <li>In fiscal year 2024, Bright Marrow Care provided more than 160,000 patient visits.</li>
      <li>Fiscal year 2024 gross annual revenue was $3.41 million, representing a 70% year-over-year growth rate from fiscal year 2023.</li>
      <li>Year-to-date gross revenue is up 3.8%, over the same period last year.</li>
    </ul>
    <p>Bright Marrow Care is led by an experienced and well-balanced leadership team which include our medical directors, management team and senior leadership team. This unique combination of backgrounds and experiences helps to inform and shape the decisions and direction of the organisation. If you would like to learn more about how we continue to keep our commitment of "creating exceptional experiences for every patient, every time", I encourage you to visit our website at <span class="lead">brightmarrowcare.ca</span>.</p>
    <p>Sincerely,<br>Dorian Hale, CEO</p>
  </div>
</section>

<section class="page" style="top:1544px">
  <div class="sidebar"><div class="page-no">2</div>
    <svg class="side-plus" viewBox="0 0 30 30" aria-hidden="true"><rect x="11" y="0" width="8" height="30" fill="var(--teal-plus)"/><rect x="0" y="11" width="30" height="8" fill="var(--teal-plus)"/></svg></div>
  <div class="content">
    <h2>About Dorian and Marisa Hale</h2>
    <p>Prior to working in the healthcare industry, Dorian spent 15 years in operations and human resources management for a large communications company. After shifting focus to the healthcare industry 9 years ago, he took on the role of Operations Manager for a pharmacy chain and was tasked with getting our first two locations built, staffed and operational. These clinics, Ridgeview Medical Clinic and Shoreline Medical Clinic, pre-dated the Bright Marrow Care name, but were the foundation upon which the organisation was built. Since then, Dorian and Marisa's combination of experience in healthcare, human resources and operations management has enabled them to grow the organisation to 4 locations with 50+ providers across 6 specialties. Dorian and Marisa's passion and dedication to improving the lives of others, whether it be our patients, employees or physicians, is evident in every aspect of our organisation and is articulated via our mission statement and core values.</p>
    <h3>Our Mission</h3>
    <p><span class="lead">Creating exceptional patient experiences for every patient, every time</span> is not just our mission statement – it's a commitment to our patients. By creating a culture where we value the quality of care every patient receives first and foremost, that empowers our employees and providers to grow, and that treats every patient with compassion, dignity and respect, we deliver on our promise to our patients.</p>
    <h3>Our History</h3>
    <p><span class="lead">Our quest to deliver consistent access to care and to provide physicians with a healthy work/life balance</span> began 9 years ago and is still the driving force behind our mission today. Bright Marrow Care started when a local pharmacist saw an opportunity to help his community that was struggling with a severe physician shortage and where thousands of people could not access care when or where they needed it. By offering physicians an operating model that gave them the ability to practice medicine without the stress of having to manage a business, a low overhead and the flexibility to practice medicine on their terms, and with the help of an experienced operations manager, he was immediately successful in attracting new physicians to the area when many others had failed. This idea became a reality when we opened our first location, Shoreline Medical Clinic, in Lake Country, BC in 2016. A year later, our second location, Ridgeview Medical Clinic opened with the same vision and the same result.</p>
    <p>In May of 2020, during the height of the pandemic, our then operations manager, Dorian Hale, approached the owner of the clinics about selling the company to him and his wife Marisa. They saw an opportunity to help thousands more people secure access to care and to help physicians find a solution to the administrative burnout that was causing so many to leave family medicine at the time. Bright Marrow Care was born.</p>
  </div>
</section>

<section class="page" style="top:2206px">
  <div class="sidebar"><div class="page-no">3</div>
    <svg class="side-plus" viewBox="0 0 30 30" aria-hidden="true"><rect x="11" y="0" width="8" height="30" fill="var(--teal-plus)"/><rect x="0" y="11" width="30" height="8" fill="var(--teal-plus)"/></svg></div>
  <svg class="decor" style="left:52px;top:18px" width="345" height="110" role="img" aria-label="Three photographs of clinic team and local scenery">
    <g fill="none" stroke="var(--teal)" stroke-width="2">
      <rect x="22" y="17" width="76" height="76" rx="14" transform="rotate(45 63 58)"/>
      <rect x="136" y="17" width="76" height="76" rx="14" transform="rotate(45 177 58)"/>
      <rect x="250" y="17" width="76" height="76" rx="14" transform="rotate(45 291 58)"/>
    </g>
    <g fill="var(--photo)">
      <rect x="18" y="14" width="76" height="76" rx="14" transform="rotate(45 56 52)"/>
      <rect x="132" y="14" width="76" height="76" rx="14" transform="rotate(45 170 52)"/>
      <rect x="246" y="14" width="76" height="76" rx="14" transform="rotate(45 284 52)"/>
    </g>
  </svg>
  <div class="content" style="top:140px">
    <p>In 2021, we opened our third location in the Pandosy neighborhood of Kelowna, the first location wearing the Bright Marrow Care name and also our first foray into multidisciplinary care with Sports Medicine and Family Practice providers working together in the same facility. Later that same year, the Cedar Run Family Medicine group joined our team and became our second Kelowna location, Bright Marrow Care – Springfield. After nearly a year of extensive renovations, the maternity care and family medicine group from Cedar Run moved into their new home and joined us at our Springfield location in early 2023.</p>
    <p>Today, Bright Marrow Care is comprised of more than 50 providers across 6 specialties and 4 locations. We are the largest, privately owned provider of primary care services in the Okanagan region and provide care to more than 80,000 residents.</p>
    <h3>Testimonials</h3>
    <p><span class="lead">We believe that our employees are our greatest asset</span>, and we strive to treat them with the same level of compassion, dignity, and respect that we provide to our patients. Employees' voices often speak the loudest about an organisation's culture. To that end, we've highlighted genuine comments submitted by our employees and providers that reflect our Mission, Values and commitment to them.</p>
    <p class="quote">I am a physician who has worked the past 47 years in Canada and the USA. One of my best experiences was to practise in Lake Country, BC at this clinic. Their amazing team made our 4 years back in Canada a wonderful experience and their model allowed me to work as hard as I wanted, but also to take time off as desired. The overhead was reasonable and the work environment was great.</p>
    <p class="quote">The leadership here went out of its way to support me and made the transition into their office a pleasure. Lake Country is one of the best areas in Canada, with plenty of nature activities year round. The only reason we returned to the US was my wife's desire to be close to our children and grandchildren. This was my choice I would still be there.</p>
    <p class="quote">During covid, the team transitioned to virtual medicine and then later to a hybrid model which I am sure will move sooner toward full in-person care. The reimbursement is fair; it is a great opportunity to adapt work to life balance and still get paid well. There is no better portion to work in the Okanagan than here.</p>
  </div>
</section>

<section class="page" style="top:2868px">
  <div class="sidebar"><div class="page-no">4</div>
    <svg class="side-plus" viewBox="0 0 30 30" aria-hidden="true"><rect x="11" y="0" width="8" height="30" fill="var(--teal-plus)"/><rect x="0" y="11" width="30" height="8" fill="var(--teal-plus)"/></svg></div>
  <div class="content">
    <p class="quote">I've had the pleasure of working with the team here since 2018 as a part-time physician. During this time, I've served both as a family doctor and locum physician, primarily at the Shoreline Medical Clinic in Lake Country, BC.</p>
    <p class="quote">Having previously co-owned three medical clinics in the Central Okanagan, I truly appreciate how this model has removed the administrative burdens that come with clinical practice. This allows me to focus solely on what I was trained to do — providing patient care.</p>
    <p class="quote">The organisation fosters a welcoming and supportive environment for physicians, tailoring opportunities to align with each doctor's unique work goals. Management is approachable, responsive, and genuinely open to suggestions from both physicians and staff, creating a culture where collaboration thrives.</p>
    <p class="quote">The clinic's EMR system is by far the most user-friendly I've encountered, further enhancing efficiency and workflow. I wholeheartedly recommend working here. The supportive atmosphere, administrative relief, and innovative leadership make it my top choice for clinical practice — I wouldn't work anywhere else.</p>
    <h3 style="line-height:1.15">About Kelowna and<br>The Okanagan Valley</h3>
    <p>If you are considering working or living in the Kelowna area, take a look at all that the Okanagan Valley has to offer.</p>
    <p>Nestled in the heart of British Columbia, the Okanagan Valley offers a lifestyle like no other. Wake up to stunning lake views, hike through breathtaking mountain trails, and spend your days exploring world-class vineyards, sandy beaches, and outdoor adventures. Whether you're living in winter, browsing in summer, or enjoying vibrant arts and local culture, the Okanagan Valley is a place to live life to the fullest. Come for the natural beauty, stay for the laid-back lifestyle!</p>
    <p style="width:190px;margin-top:12px">Kelowna has experienced a population growth of 14% since 2016, making it the fastest growing metropolitan area in Canada. With over 165,000 residents, and a median age of 42, it is also the 6th largest, and one of the youngest cities in the province of British Columbia. Situated in the heart of the Okanagan Valley, Kelowna is surrounded by mountains, lakes and vineyards where residents embrace outdoor adventures and an active lifestyle all year long. The city is also an economic powerhouse, home to robust traditional sectors like agriculture and construction, and burgeoning new sectors such as information technology.</p>
  </div>
  <svg class="decor" style="left:248px;top:430px" width="150" height="140" role="img" aria-label="Aerial photograph of Kelowna and Okanagan Lake">
    <defs><linearGradient id="lake1" x1="0" y1="0" x2="0" y2="1"><stop offset="0" stop-color="#9fb4c4"/><stop offset="1" stop-color="#5d6b5a"/></linearGradient></defs>
    <rect x="32" y="22" width="96" height="96" rx="18" transform="rotate(45 80 70)" fill="none" stroke="var(--teal)" stroke-width="2"/>
    <rect x="28" y="18" width="96" height="96" rx="18" transform="rotate(45 76 66)" fill="url(#lake1)"/>
  </svg>
</section>

<section class="page" style="top:3527px">
  <div class="sidebar"><div class="page-no">5</div>
    <svg class="side-plus" viewBox="0 0 30 30" aria-hidden="true"><rect x="11" y="0" width="8" height="30" fill="var(--teal-plus)"/><rect x="0" y="11" width="30" height="8" fill="var(--teal-plus)"/></svg></div>
  <svg class="decor" style="left:250px;top:36px" width="150" height="140" role="img" aria-label="Photograph of Kelowna city and lakeshore at sunset">
    <defs><linearGradient id="lake2" x1="0" y1="0" x2="0" y2="1"><stop offset="0" stop-color="#e6c9a3"/><stop offset=".5" stop-color="#7d8fa8"/><stop offset="1" stop-color="#4f5a4c"/></linearGradient></defs>
    <rect x="32" y="22" width="96" height="96" rx="18" transform="rotate(45 80 70)" fill="none" stroke="var(--teal)" stroke-width="2"/>
    <rect x="28" y="18" width="96" height="96" rx="18" transform="rotate(45 76 66)" fill="url(#lake2)"/>
  </svg>
  <div class="content">
    <h2>Healthcare<span class="ghost" style="left:70px">Healthcare</span></h2>
    <div class="sub">Climate and Outdoor Recreation</div>
    <div class="intro-text"><p>The Okanagan Valley offers an abundance of outdoor activities ranging from water sports in the summer to skiing in the winter, as well as hiking, biking, and opportunities for relaxation and nature immersion. Kelowna is a great place for year-round outdoor adventure, including 35 provincial parks, more than 100 lakes, same-day access to 5 world class ski resorts and 186 wineries.</p></div>
    <p>With over 2,000 hours of sunshine a year, the Okanagan Valley boasts one of the best climates in Canada. Enjoy warm, dry summers ideal for outdoor activities, relaxing at lakeside beaches, and exploring vineyards. Winters bring a beautiful balance of mild temperatures and snowy mountain peaks — famous for their light champagne powder. Whether you'd like a sun-seeker or snow lover, the Okanagan offers the ideal climate year-round with average daytime high temperatures ranging from 2°C (36°F) in January to 28°C (82°F) in July.</p>
    <h3>Things to do</h3>
  </div>
  <svg class="decor" style="left:52px;top:372px" width="345" height="105" role="img" aria-label="Three photographs of local activities: canyon trail, ski hill and vineyard">
    <defs>
      <linearGradient id="act1" x1="0" y1="0" x2="0" y2="1"><stop offset="0" stop-color="#b98a5e"/><stop offset="1" stop-color="#6d4a2f"/></linearGradient>
      <linearGradient id="act2" x1="0" y1="0" x2="0" y2="1"><stop offset="0" stop-color="#c9d6e0"/><stop offset="1" stop-color="#6d7c8a"/></linearGradient>
      <linearGradient id="act3" x1="0" y1="0" x2="0" y2="1"><stop offset="0" stop-color="#a9c3cf"/><stop offset="1" stop-color="#5c7a3e"/></linearGradient>
    </defs>
    <g fill="none" stroke="var(--teal)" stroke-width="2">
      <rect x="22" y="17" width="72" height="72" rx="14" transform="rotate(45 60 55)"/>
      <rect x="136" y="17" width="72" height="72" rx="14" transform="rotate(45 174 55)"/>
      <rect x="250" y="17" width="72" height="72" rx="14" transform="rotate(45 288 55)"/>
    </g>
    <rect x="18" y="14" width="72" height="72" rx="14" transform="rotate(45 54 50)" fill="url(#act1)"/>
    <rect x="132" y="14" width="72" height="72" rx="14" transform="rotate(45 168 50)" fill="url(#act2)"/>
    <rect x="246" y="14" width="72" height="72" rx="14" transform="rotate(45 282 50)" fill="url(#act3)"/>
  </svg>
  <div class="content" style="top:490px">
    <div class="cols">
      <div><div class="list-title">Attractions</div>
        <ul class="mini"><li>Valley Aviation Heritage Centre</li><li>Valley Discovery Centre</li><li>Lakeside Cellar Tours and Tastings</li><li>Lakeside Golf Courses</li><li>Sunfield Petting Farm</li><li>Lakeshore Rail Trail</li><li>The Lake and Beaches</li><li>Lakefront Events Arena</li></ul></div>
      <div><div class="list-title">Parks</div>
        <ul class="mini"><li>Fir Creek Park</li><li>Bluewater Lake Park</li><li>Ridge Summit Park</li><li>Canyon Trestle Park</li><li>Downtown City Park</li><li>Creekside Regional Park</li><li>Highland Mountain Park</li></ul></div>
    </div>
  </div>
</section>

<section class="page" style="top:4187px">
  <div class="sidebar"><div class="page-no">6</div>
    <svg class="side-plus" viewBox="0 0 30 30" aria-hidden="true"><rect x="11" y="0" width="8" height="30" fill="var(--teal-plus)"/><rect x="0" y="11" width="30" height="8" fill="var(--teal-plus)"/></svg></div>
  <svg class="decor" style="left:270px;top:450px" width="110" height="110" aria-hidden="true"><rect x="38" y="0" width="34" height="110" fill="var(--teal-faint)"/><rect x="0" y="38" width="110" height="34" fill="var(--teal-faint)"/></svg>
  <div class="content">
    <div class="cols" style="margin-bottom:14px">
      <div><div class="list-title">Arts</div>
        <ul class="mini"><li>Valley Symphony Orchestra</li><li>Lakeshore Art Gallery</li><li>Harbourline Arts Centre</li><li>Community Actors Theatre</li><li>Regional Heritage Museum</li><li>Wine and Orchard Museum</li></ul></div>
      <div><div class="list-title">Events</div>
        <ul class="mini"><li>Lakeside Rock Weekend</li><li>Open Water Lake Swim</li><li>Summer Street Festival</li><li>Harvest Wine Week</li><li>Orchard Triathlon</li></ul></div>
    </div>
    <div class="cols" style="margin-bottom:18px">
      <div><div class="list-title">Higher Education</div>
        <ul class="mini"><li>Valley Regional University</li><li>Lakeview Community College</li><li>Creative Arts and Media School</li><li>Interior Technical Institute</li></ul></div>
      <div><div class="list-title">Sports</div>
        <ul class="mini"><li>Junior Hockey Club</li><li>Collegiate Baseball Club</li><li>Amateur Football Club</li><li>Community Basketball League</li></ul></div>
    </div>
    <h3>Additional Information</h3>
    <div class="sub">Bright Marrow Care</div>
    <div class="links">https://brightmarrowcare.ca/about-us/<br>https://brightmarrowcare.ca/clinics/<br>https://brightmarrowcare.ca/specialties/<br>https://brightmarrowcare.ca/careers/</div>
    <div class="sub" style="margin-top:10px">Kelowna</div>
    <div class="links">https://www.lakecitychamber.example/<br>https://www.visitlakecity.example/<br>https://okvalleyski.example/<br><br>https://www.bcwinetrail.example/<br>https://www.lakecity.example/<br>https://www.regionstats.example/</div>
  </div>
</section>

</body>
</html>
```